Meadowlark Cleaning Services - Redesign

I've got my website designed a few years ago and it looks dated now. I would like to get a modern, happy, bright, and clean look. All the content needed can be found at my current website www.meadowlarkcs.example. Not necessarily need to use all of it, since I want something more clean and easy to read.
I need a 5 pages website:
HOME | SERVICES | ESTIMATE |TESTIMONIALS | CONTACT US

Industry/Entity Type

Janitorial Service

Number of Pages Required

5+ page

Colors
0792cd
34a6d7
85cae6
cee9f5
ebebeb
f0f0f0
f5f5f5
b1b1b1
000000

Requirements
Must have
• Who we are?
• Meadowlark Cleaning Services is a local, family-owned, client-focused house and office cleaning company that strives to ensure the highest level of customer satisfaction. We offer expert residential and commercial cleaning services to all the Seattle and Eastside areas.
• Why Meadowlark?
• √ We are insured, bonded and licensed.
•  Meadowlark Cleaning Service is Fully Insured so you can rest easy knowing your home is protected.
•  Copy of insurance available upon request.
•

√ We provide all supplies and equipments needed to thoroughly clean your home or business.

• √ We are not a franchise. We are a local, family-owned company.

• When you call Meadowlark Cleaning Services, you’ll always speak to one of the owners, which is a great benefit to you since this allows us to give you the personal attention and more time needed to clean your home the way you want it cleaned.

• √ We are good at what we do, and we like doing it.

```html
<!DOCTYPE html>
<html lang="en">
<head>
<meta charset="utf-8">
<title>Meadowlark Cleaning Services – Testimonials</title>
<link rel="stylesheet" href="https://fonts.googleapis.com/css2?family=Montserrat:wght@400;600&family=Great+Vibes&family=Roboto:wght@400;500&display=swap">
<style>
:root{
  --brand:#0792cd;
  --brand-mid:#34a6d7;
  --brand-light:#85cae6;
  --brand-pale:#cee9f5;
  --grey-line:#b1b1b1;
  --grey-bg:#f5f5f5;
  --ink:#000000;
  --text:#555555;
  --footer:#2b2b2b;
  --white:#ffffff;
}
*{margin:0;padding:0;box-sizing:border-box}
html,body{width:775px;height:1200px;overflow:hidden;background:var(--white)}
body{font-family:"Roboto",Arial,sans-serif;position:relative}
.page{position:relative;width:775px;height:1200px;overflow:hidden}
.abs{position:absolute}

.hero-photo{left:0;top:0;width:775px;height:440px;
  background:linear-gradient(180deg,#eef4f8 0%,#dfe6ec 45%,#c9ced4 75%,#b9bec4 100%)}
.shapes{left:0;top:0}

.main-nav{top:20px;left:0;width:775px;height:16px}
.main-nav a{position:absolute;transform:translateX(-50%);font:600 11px "Montserrat",sans-serif;color:var(--brand);text-decoration:none;white-space:nowrap}

.hero-name{left:0;top:172px;width:775px;text-align:center;color:var(--brand);font:600 36px/1 "Montserrat",sans-serif}
.hero-name small{display:block;font-size:11px;letter-spacing:1px;margin-top:6px}

.intro-title{top:430px;left:0;width:775px;text-align:center;font:400 24px "Montserrat",sans-serif;color:#1da1e0}
.intro-script{top:459px;left:0;width:775px;text-align:center;font:400 15px "Great Vibes",cursive;color:#222}
.intro-text{top:490px;left:120px;width:535px;text-align:center;font:400 9.6px/14.5px Arial,sans-serif;color:var(--text)}

.field{border:1px solid #c8c8c8;background:var(--white);font:400 9.5px Arial,sans-serif;color:#444;padding:0 7px;display:flex;align-items:center}
.field.area{align-items:flex-start;padding-top:10px}
.field .caret{position:absolute;right:8px;top:13px}
.submit{left:332px;top:757px;width:110px;height:33px;background:var(--brand);color:var(--white);font:400 13px "Montserrat",sans-serif;display:flex;align-items:center;justify-content:center}

.clients-title{top:887px;left:0;width:775px;text-align:center;font:400 24px "Montserrat",sans-serif;color:var(--ink)}
.clients-title span{color:var(--white)}
.clients-script{top:917px;left:0;width:775px;text-align:center;font:400 15px "Great Vibes",cursive;color:#1a1a1a}
.quote-box{left:152px;top:955px;width:471px;height:67px;background:var(--white);border-radius:3px;font:400 9.4px/15px Arial,sans-serif;color:#444;text-align:center;padding:9px 30px}
.quote-name{top:1040px;left:0;width:775px;text-align:center;color:var(--white);font:400 17px "Montserrat",sans-serif}
.quote-name em{font-size:12px;font-style:italic}

.site-footer{left:0;top:1124px;width:775px;height:76px;background:var(--footer)}
.footer-nav{position:absolute;left:50px;top:19px;display:flex}
.footer-nav a{font:400 9.5px Arial,sans-serif;color:var(--white);text-decoration:none;padding:0 10px;border-left:1px solid #555;line-height:16px}
.footer-nav a:first-child{padding-left:0;border-left:none}
.copyright{position:absolute;left:50px;top:45px;font:400 9.5px Arial,sans-serif;color:var(--white)}
.copyright span{color:var(--brand-mid)}
.footer-name{position:absolute;right:52px;top:22px;font:600 24px/1 "Montserrat",sans-serif;color:#8d8d8d;text-align:center}
.footer-name small{display:block;font-size:7px;letter-spacing:1px;margin-top:3px}
</style>
</head>
<body>
<div class="page">
  <div class="abs hero-photo" role="img" aria-label="Photo of a smiling family giving thumbs up on a sofa"></div>

  <svg class="abs shapes" width="775" height="1200" viewBox="0 0 775 1200" aria-hidden="true">
    <polygon points="0,437 388,368 775,437 775,900 0,900" fill="#ffffff"/>
    <polygon points="0,895 388,828 775,895 775,1124 0,1124" fill="#000"/>
    <polygon points="0,903 388,836 775,903 775,1124 0,1124" fill="#2bafe8"/>
  </svg>
  <div class="abs" style="left:0;top:836px;width:775px;height:288px;clip-path:polygon(0 67px,388px 0,775px 67px,775px 288px,0 288px);background:linear-gradient(180deg,#3bb6ec,#1ea6e3)" role="img" aria-label="Mosaic of client portrait photos tinted blue"></div>

  <nav class="abs main-nav">
    <a style="left:206px">HOME</a>
    <a style="left:278px">SERVICES</a>
    <a style="left:358px">ESTIMATE</a>
    <a style="left:449px">TESTIMONIALS</a>
    <a style="left:550px">CONTACT US</a>
  </nav>

  <div class="abs hero-name">Meadowlark<small>CLEANING SERVICES</small></div>

  <h1 class="abs intro-title">Are We Meeting Your Expectations?</h1>
  <div class="abs intro-script">Testimonial</div>
  <p class="abs intro-text">Customer service and high quality workmanship are key values at Meadowlark Cleaning Services. We listen to what our customers say and we welcome your feedback on how we are meeting your needs. Please let us know how we are doing.</p>

  <div class="abs field" style="left:101px;top:553px;width:552px;height:30px">Enter Name</div>
  <div class="abs field" style="left:101px;top:596px;width:269px;height:30px">Enter Email</div>
  <div class="abs field" style="left:383px;top:596px;width:270px;height:30px">Enter City</div>
  <div class="abs field" style="left:101px;top:639px;width:269px;height:30px">Service Frequency
    <svg class="caret" width="10" height="6" viewBox="0 0 10 6"><polygon points="0,0 10,0 5,6" fill="var(--brand)"/></svg></div>
  <div class="abs field" style="left:383px;top:639px;width:270px;height:30px">Satisfaction
    <svg class="caret" width="10" height="6" viewBox="0 0 10 6"><polygon points="0,0 10,0 5,6" fill="var(--brand)"/></svg></div>
  <div class="abs field area" style="left:101px;top:683px;width:552px;height:60px">Comments</div>
  <div class="abs submit">SUBMIT</div>

  <h2 class="abs clients-title">WHAT <span>CLIENTS</span></h2>
  <div class="abs clients-script">Say About Us</div>
  <div class="abs quote-box">"The folks at Meadowlark are congenial and very personable, yet at the same time very professional. They keep their appointments, and they clean thoroughly and efficiently. Meadowlark has been a real blessing to our family!"</div>
  <svg class="abs" style="left:382px;top:1021px" width="12" height="7" viewBox="0 0 12 7" aria-hidden="true"><polygon points="0,0 12,0 6,7" fill="#fff"/></svg>
  <div class="abs quote-name">Daniel R., <em>Redmond-WA (Lakeview)</em></div>

  <footer class="abs site-footer">
    <nav class="footer-nav"><a>HOME</a><a>SERVICES</a><a>ESTIMATE</a><a>TESTIMONIALS</a><a>CONTACT US</a></nav>
    <p class="copyright">© <span>MEADOWLARK CLEANING SERVICES</span> - 2016, All rights resreved</p>
    <div class="footer-name">Meadowlark<small>CLEANING SERVICES</small></div>
  </footer>
</div>
</body>
</html>
```